Tre Nuvole Leaf Design Business Card/Hang Tag

Design a 3.5" X 2" (Leaf Shaped-See Files) Business Card/ Hang Tag that will have our Business Logo and Info on the Front, and will have On-Line Delivery Logos and Info on the Rear.

```html
<!DOCTYPE html>
<html lang="en">
<head>
<meta charset="utf-8">
<title>Tre Nuvole – Leaf Business Card</title>
<link rel="stylesheet" href="https://fonts.googleapis.com/css2?family=Cinzel:wght@600&family=Lato:wght@400;700&display=swap">
<style>
  :root {
    --stage: #1e1e1e;
    --paper: #ffffff;
    --green: #1f4a24;
    --red: #d6202d;
    --ink: #3a3a3a;
    --delivery-green: #3f9a4a;
  }
  * { box-sizing: border-box; margin: 0; padding: 0; }
  html, body { width: 979px; height: 1200px; overflow: hidden; }
  body {
    background: var(--stage);
    font-family: "Lato", sans-serif;
    position: relative;
  }
  .leaf-card {
    position: absolute;
    left: 126px;
    width: 756px;
    height: 432px;
    background: var(--paper);
    border-radius: 210px 0 210px 0 / 220px 0 220px 0;
  }
  .leaf-card--back { top: 102px; }
  .leaf-card--front { top: 642px; }

  .brand-mark {
    position: absolute;
    transform: translate(-50%, -50%);
    display: flex;
    align-items: center;
    gap: 10px;
    color: var(--green);
    font-family: "Cinzel", serif;
    font-weight: 600;
    font-size: 30px;
    white-space: nowrap;
  }
  .brand-mark__dot {
    width: 16px; height: 16px;
    border-radius: 50%;
    background: var(--red);
  }
  .leaf-card--back .brand-mark { left: 378px; top: 162px; }
  .leaf-card--front .brand-mark { left: 558px; top: 162px; }

  .delivery-partner {
    position: absolute;
    top: 342px;
    transform: translate(-50%, -50%);
    display: flex;
    align-items: center;
    gap: 8px;
    font-weight: 700;
    font-size: 20px;
    white-space: nowrap;
  }
  .delivery-partner__dot { width: 22px; height: 22px; border-radius: 50%; }
  .delivery-partner--fork { left: 91px; color: var(--delivery-green); }
  .delivery-partner--fork .delivery-partner__dot { background: var(--delivery-green); }
  .delivery-partner--dish { left: 324px; color: var(--red); }
  .delivery-partner--dish .delivery-partner__dot { background: var(--red); }
  .delivery-partner--porch { left: 546px; color: var(--red); }
  .delivery-partner--porch .delivery-partner__dot { background: var(--red); }

  .person { position: absolute; left: 56px; top: 192px; }
  .person__name {
    font-family: "Cinzel", serif;
    font-weight: 600;
    font-size: 33px;
    color: var(--green);
    line-height: 1.1;
    letter-spacing: 0.5px;
  }
  .person__role {
    font-size: 17px;
    color: var(--red);
    line-height: 1.2;
  }
  .person__rule {
    width: 72px;
    height: 2px;
    background: var(--green);
    margin-top: 3px;
  }

  .contact-list {
    position: absolute;
    left: 56px;
    top: 318px;
    list-style: none;
    color: var(--ink);
    font-size: 17px;
  }
  .contact-list li {
    display: flex;
    align-items: center;
    gap: 10px;
    height: 22px;
    margin-bottom: 2px;
  }
  .contact-list li:first-child { margin-bottom: 8px; }
  .contact-list svg { width: 13px; height: 13px; flex: none; }

  .address {
    position: absolute;
    left: 423px;
    top: 340px;
    font-size: 17px;
    line-height: 21px;
    color: var(--ink);
    font-style: normal;
  }
</style>
</head>
<body>

  <section class="leaf-card leaf-card--back" aria-label="Card back: delivery partners">
    <div class="brand-mark"><span class="brand-mark__dot"></span>Tre Nuvole</div>
    <div class="delivery-partner delivery-partner--fork"><span class="delivery-partner__dot"></span>Fork Run</div>
    <div class="delivery-partner delivery-partner--dish"><span class="delivery-partner__dot"></span>DishHop</div>
    <div class="delivery-partner delivery-partner--porch"><span class="delivery-partner__dot"></span>PorchDrop</div>
  </section>

  <section class="leaf-card leaf-card--front" aria-label="Card front: contact details">
    <div class="person">
      <h1 class="person__name">MARCO BELLINI</h1>
      <p class="person__role">Director</p>
      <div class="person__rule"></div>
    </div>

    <ul class="contact-list">
      <li>
        <svg viewBox="0 0 16 16" aria-hidden="true"><path fill="#d6202d" d="M3.6 1.5l2.3 2.4-1.2 1.8c.9 2 2.5 3.7 4.6 4.7l1.8-1.2 2.4 2.3-1.4 2.2C6.7 13.4 2.6 9.3 1.4 3l2.2-1.5z"/></svg>
        (650) 555-0148
      </li>
      <li>
        <svg viewBox="0 0 16 16" aria-hidden="true"><rect x="1" y="3" width="14" height="10" rx="1" fill="#d6202d"/><path d="M1.5 4l6.5 5 6.5-5" stroke="#fff" stroke-width="1.4" fill="none"/></svg>
        marco@trenuvolerestaurant.com
      </li>
      <li>
        <svg viewBox="0 0 16 16" aria-hidden="true"><g fill="none" stroke="#d6202d" stroke-width="1.4"><circle cx="8" cy="8" r="6.5"/><ellipse cx="8" cy="8" rx="3" ry="6.5"/><path d="M1.5 8h13M2.5 5h11M2.5 11h11"/></g></svg>
        www.trenuvolerestaurant.com
      </li>
    </ul>

    <address class="address">418 Linden Avenue, Larkfield<br>California 94090</address>

    <div class="brand-mark"><span class="brand-mark__dot"></span>Tre Nuvole</div>
  </section>

</body>
</html>
```